Business Card Design

Business Card for professional consulting firm working with large financial institutions.

Target Market(s)

Executive buyers

Industry/Entity Type

Banking

Contact Information for Business Card

Mild creativity wanted. Not boring, but do elaborate artwork.

Font styles to use
Serif
Sans Serif

Colors

Designer to choose colors to be used in the design.

Requirements
Must have
• Standard business card features - company name, individual name, telephone, website, email, locations.
Nice to have
• Two colors
Should not have
• too many colors, fancy printing, cartoons.

```html
<!DOCTYPE html>
<html lang="en">
<head>
<meta charset="utf-8">
<title>Northvale Advisory – Business Cards</title>
<link href="https://fonts.googleapis.com/css2?family=Lora:wght@400&family=Montserrat:wght@400;500;700;800&display=swap" rel="stylesheet">
<style>
  :root {
    --charcoal: #2b2b2b;
    --paper: #f7f7f7;
    --silver: #c4c4c4;
    --ink: #3a3a3a;
    --light-text: #e8e8e8;
    --backdrop: #ececec;
  }
  * { margin: 0; padding: 0; box-sizing: border-box; }
  html, body { width: 1200px; height: 1171px; overflow: hidden; }
  body {
    background: var(--backdrop);
    font-family: "Montserrat", sans-serif;
    display: flex;
    flex-direction: column;
    align-items: center;
    justify-content: center;
    gap: 70px;
  }
  .card {
    position: relative;
    width: 840px;
    height: 480px;
    box-shadow: 0 10px 30px rgba(0,0,0,0.12);
    overflow: hidden;
  }
  .card-shape { position: absolute; inset: 0; }
  .brand-name {
    font-family: "Lora", serif;
    font-weight: 400;
    letter-spacing: 1px;
    white-space: nowrap;
  }

  /* Front card */
  .front-card { background: var(--charcoal); }
  .front-brand {
    position: absolute;
    left: 50px; top: 95px;
    width: 400px;
    text-align: center;
  }
  .front-brand .brand-name { font-size: 40px; color: var(--ink); }
  .locations {
    margin-top: 30px;
    font-size: 17px;
    letter-spacing: 2px;
    color: var(--ink);
  }
  .contact-block {
    position: absolute;
    left: 520px; top: 250px;
    color: var(--light-text);
  }
  .person-name { font-size: 30px; font-weight: 800; color: #fff; }
  .person-title { font-size: 16px; font-weight: 500; margin-top: 2px; }
  .divider { width: 60px; height: 1px; background: #888; margin: 22px 0 16px; }
  .contact-row {
    display: flex; align-items: center; gap: 14px;
    font-size: 16px; margin-top: 8px;
    white-space: nowrap;
  }
  .contact-row svg { width: 16px; height: 16px; flex: none; }

  /* Back card */
  .back-card {
    background: var(--charcoal);
    display: flex; flex-direction: column;
    align-items: center; justify-content: center;
  }
  .back-card .brand-name { font-size: 64px; color: #fff; }
  .website {
    margin-top: 40px;
    font-size: 18px;
    letter-spacing: 3px;
    color: var(--light-text);
  }
</style>
</head>
<body>

  <section class="card front-card" aria-label="Business card front">
    <svg class="card-shape" viewBox="0 0 840 480" preserveAspectRatio="none" aria-hidden="true">
      <path d="M0 0 H585 Q560 330 300 480 H0 Z" fill="var(--silver)"/>
      <path d="M0 0 H555 Q520 315 270 480 H0 Z" fill="var(--paper)"/>
    </svg>
    <div class="front-brand">
      <div class="brand-name">Northvale Advisory</div>
      <div class="locations">DENVER • BOSTON, MA</div>
    </div>
    <div class="contact-block">
      <div class="person-name">Daniel HART</div>
      <div class="person-title">Managing Director</div>
      <div class="divider"></div>
      <div class="contact-row">
        <svg viewBox="0 0 16 16" aria-hidden="true"><path d="M4 1.5 L6.5 5 L5 6.5 Q6.5 9.5 9.5 11 L11 9.5 L14.5 12 L13 14.5 Q6 14 1.5 3 Z" fill="none" stroke="currentColor" stroke-width="1.3" stroke-linejoin="round"/></svg>
        <span>000.000.0000</span>
      </div>
      <div class="contact-row">
        <svg viewBox="0 0 16 16" aria-hidden="true"><rect x="1" y="3" width="14" height="10" fill="none" stroke="currentColor" stroke-width="1.3"/><path d="M1 3 L8 9 L15 3" fill="none" stroke="currentColor" stroke-width="1.3"/></svg>
        <span>daniel@northvaleadvisory.com</span>
      </div>
    </div>
  </section>

  <section class="card back-card" aria-label="Business card back">
    <div class="brand-name">Northvale Advisory</div>
    <div class="website">www.northvaleadvisory.us</div>
  </section>

</body>
</html>
```